Oven Cleaning Business owner needs business card design

Hi there,
Would like for a business card to be designed for myself, the owner of a professional oven cleaning business on the Sunshine Coast.
Would like it to look sleek, and modern-ish. Bit creative is encouraged too.
Include following:
Name/title: Corin ter Haghe, Owner
Phone number: 1300 482 916
Email: info@hearthshinecrew.com.au
Website: www.hearthshinecrew.com.au

```html
<!DOCTYPE html>
<html lang="en">
<head>
<meta charset="utf-8">
<title>Hearthshine Crew – Business Card</title>
<link href="https://fonts.googleapis.com/css2?family=Montserrat:wght@400;500;700;800&display=swap" rel="stylesheet">
<style>
  :root {
    --backdrop: #2a2b30;
    --navy: #273369;
    --teal: #4cbfcc;
    --ink: #1b1c20;
    --paper: #ffffff;
    --faint: #eef3f5;
  }
  * { margin: 0; padding: 0; box-sizing: border-box; }
  html, body { width: 1200px; height: 900px; overflow: hidden; }
  body {
    background: var(--backdrop);
    font-family: "Montserrat", Arial, sans-serif;
    position: relative;
  }
  .card {
    position: absolute;
    left: 290px;
    width: 620px;
    height: 354px;
    border-radius: 22px;
    overflow: hidden;
    box-shadow: 0 18px 40px rgba(0,0,0,0.45);
  }
  .card-front { top: 64px; background: var(--navy); }
  .card-back { top: 482px; background: var(--paper); }

  .brand {
    display: flex;
    align-items: center;
    gap: 14px;
  }
  .brand-dot {
    border-radius: 50%;
    background: var(--teal);
    flex: none;
  }
  .brand-name {
    font-weight: 800;
    color: var(--teal);
    text-transform: uppercase;
    letter-spacing: 0.04em;
    line-height: 1;
  }
  .card-front .brand {
    position: absolute;
    left: 50%; top: 50%;
    transform: translate(-50%, -50%);
  }
  .card-front .brand-dot { width: 58px; height: 58px; }
  .card-front .brand-name { font-size: 38px; color: var(--paper); }

  .card-back .watermark {
    position: absolute;
    right: -40px; top: -30px;
    width: 300px; height: 300px;
    border-radius: 50%;
    background: var(--faint);
  }
  .card-back .brand {
    position: absolute;
    left: 40px; top: 40px;
  }
  .card-back .brand-dot { width: 34px; height: 34px; }
  .card-back .brand-name { font-size: 24px; color: var(--ink); }

  .holder {
    position: absolute;
    left: 40px; top: 150px;
  }
  .holder-name {
    font-size: 30px;
    font-weight: 700;
    color: var(--teal);
    letter-spacing: -0.01em;
  }
  .holder-title {
    font-size: 15px;
    font-weight: 400;
    color: var(--ink);
    margin-top: 2px;
  }
  .rule {
    position: absolute;
    left: 40px; right: 0; top: 232px;
    height: 2px;
    background: var(--teal);
  }
  .contacts {
    position: absolute;
    left: 40px; top: 248px;
    list-style: none;
  }
  .contacts li {
    display: flex;
    align-items: center;
    gap: 10px;
    font-size: 14px;
    color: var(--ink);
    line-height: 26px;
  }
  .contacts svg { width: 13px; height: 13px; fill: var(--teal); flex: none; }
</style>
</head>
<body>
  <section class="card card-front" aria-label="Card front">
    <div class="brand">
      <span class="brand-dot"></span>
      <span class="brand-name">Hearthshine Crew</span>
    </div>
  </section>

  <section class="card card-back" aria-label="Card back">
    <div class="watermark" role="img" aria-label="Faint brand backdrop"></div>
    <div class="brand">
      <span class="brand-dot"></span>
      <span class="brand-name">Hearthshine Crew</span>
    </div>
    <div class="holder">
      <p class="holder-name">Corin ter Haghe</p>
      <p class="holder-title">Owner</p>
    </div>
    <div class="rule"></div>
    <ul class="contacts">
      <li>
        <svg viewBox="0 0 16 16" aria-hidden="true"><path d="M3.6 1.2l2.3 2.7-1.3 1.8c.9 2 2.5 3.6 4.6 4.6l1.8-1.3 2.7 2.3-1.2 2.5C7 13.6 2.4 9 1.2 2.4z"/></svg>
        1300 482 916
      </li>
      <li>
        <svg viewBox="0 0 16 16" aria-hidden="true"><path d="M1 3h14v10H1zm1.5 1.3v.4L8 8.6l5.5-3.9v-.4z"/></svg>
        info@hearthshinecrew.com.au
      </li>
      <li>
        <svg viewBox="0 0 16 16" aria-hidden="true"><path d="M8 1a7 7 0 100 14A7 7 0 008 1zm0 1.5c.8 0 1.7 1.6 2 4H6c.3-2.4 1.2-4 2-4zM2.6 6.5h2c-.1.5-.1 1-.1 1.5s0 1 .1 1.5h-2a5.6 5.6 0 010-3zm3.4 3h4c-.3 2.4-1.2 4-2 4s-1.7-1.6-2-4zm5.4 0c.1-.5.1-1 .1-1.5s0-1-.1-1.5h2a5.6 5.6 0 010 3z"/></svg>
        www.hearthshinecrew.com.au
      </li>
    </ul>
  </section>
</body>
</html>
```